Web design for a crypto donation landing page for wildlife protection projects

We are developing the landing page for the presale of a web3 project, which will collect cryptos to send them to wildlife protection projects.
Here some website we like:
https://www.tidegroveaccord.fr/
https://qelvo.io/
https://www.mossvalen.io/
please, use the wireframe to know what blocks we want but we accept different template.
If possible, do the design on figma. Use 1 or 2 fonts max. Used green, blue and white, no more. Make a consistent system design by using the same font size for H1, H2, H3... and the same colors everywhere.

```html
<!DOCTYPE html>
<html lang="fr">
<head>
<meta charset="utf-8">
<title>Germinea – Protegeons la nature ensemble</title>
<link href="https://fonts.googleapis.com/css2?family=Poppins:wght@400;500;600;700&display=swap" rel="stylesheet">
<style>
:root{
  --blue:#2a1a8e;
  --blue-deep:#1d1070;
  --green:#3aac1f;
  --green-light:#8fd12b;
  --white:#ffffff;
  --ink:#25176f;
  --muted:#6b6790;
  --line:#d9d6ec;
}
*{box-sizing:border-box;margin:0;padding:0}
html,body{width:1200px;height:4188px;overflow:hidden}
body{font-family:'Poppins',sans-serif;color:var(--ink);background:var(--white);position:relative}
.abs{position:absolute}
h1,h2,h3{font-weight:700;line-height:1.15}
.h2{font-size:34px}
.h3{font-size:18px;font-weight:600}

/* hero */
.hero{left:0;top:0;width:1200px;height:740px;background:linear-gradient(180deg,var(--blue-deep),var(--blue))}
.brand{display:flex;align-items:center;gap:10px;font-weight:700;font-size:24px;color:var(--green-light)}
.brand-dot{width:28px;height:28px;border-radius:50%;background:var(--green)}
.nav{right:200px;top:28px;display:flex;gap:34px;font-size:14px;font-weight:500;color:var(--white)}
.hero h1{left:60px;top:110px;width:520px;font-size:54px;color:var(--white)}
.hero-lead{left:60px;top:255px;width:480px;font-size:20px;font-weight:600;color:var(--green-light);line-height:1.35}
.hero-text{left:60px;top:330px;width:500px;font-size:14px;color:var(--white);line-height:1.6;opacity:.9}
.partners{left:60px;top:460px;display:flex;gap:44px;align-items:center;font-size:22px;font-weight:700;color:var(--white)}
.buy{left:680px;top:60px;width:300px;height:240px;border-radius:22px;background:linear-gradient(160deg,var(--green-light),var(--green));padding:26px;color:var(--white);text-align:center;box-shadow:0 20px 40px rgba(0,0,0,.25)}
.buy h3{font-size:20px;font-weight:600}
.counter{margin:18px auto 0;width:220px;height:44px;border-radius:22px;background:var(--white);display:flex;align-items:center;justify-content:space-between;padding:0 6px;color:var(--ink);font-weight:600;font-size:18px}
.counter span.btn{width:32px;height:32px;border-radius:50%;background:var(--blue);color:var(--white);display:flex;align-items:center;justify-content:center}
.buy .price{margin-top:18px;font-size:22px;font-weight:700}
.buy .cta{margin:16px auto 0;width:150px;height:42px;border-radius:21px;background:var(--blue);display:flex;align-items:center;justify-content:center;font-weight:600;font-size:15px}
.forest{left:0;top:520px;width:1200px;height:220px;background:linear-gradient(180deg,rgba(42,26,142,0),#180b5c)}

/* how */
.how-title{left:0;top:790px;width:1200px;text-align:center;color:var(--ink)}
.step{width:300px;height:300px;border-radius:50%;text-align:center;padding:80px 40px 0}
.step.outline{border:2px dashed var(--blue);background:var(--white)}
.step.filled{background:linear-gradient(160deg,var(--green-light),var(--green));color:var(--white);width:320px;height:320px;padding:90px 44px 0}
.step-icon{position:absolute;left:50%;top:-30px;transform:translateX(-50%);width:70px;height:70px;border-radius:50%;background:var(--blue);border:6px solid var(--white);display:flex;align-items:center;justify-content:center}
.step p{margin-top:10px;font-size:12px;line-height:1.6;color:var(--muted)}
.step.filled p{color:var(--white)}

/* community */
.community{left:0;top:1330px;width:1200px;height:620px;background:var(--blue)}
.community h2{left:140px;top:70px;width:560px;color:var(--white);font-size:32px}
.community .lead{left:140px;top:170px;width:480px;font-size:16px;font-weight:600;color:var(--green-light);line-height:1.5}
.community .sub{left:140px;top:250px;width:480px;font-size:14px;font-weight:600;color:var(--white)}
.community ul{left:140px;top:284px;width:500px;list-style:none;font-size:13px;color:var(--white);line-height:2}
.community li::before{content:"";display:inline-block;width:10px;height:10px;border-radius:2px;background:var(--green-light);margin-right:10px}
.laptop{left:740px;top:80px;width:340px;height:230px;border-radius:14px;background:linear-gradient(160deg,#3d2ba8,#1b0f62)}
.channels{left:790px;top:180px;display:flex;gap:40px;color:var(--white);font-size:18px;font-weight:600}
.community-forest{left:0;top:420px;width:1200px;height:200px;background:linear-gradient(180deg,rgba(42,26,142,0),#160a55)}

/* roadmap */
.roadmap{left:100px;top:1880px;width:980px;height:580px;border-radius:26px;background:linear-gradient(135deg,var(--green-light),var(--green));color:var(--white)}
.roadmap h2{left:0;top:30px;width:980px;text-align:center;font-size:30px}
.roadmap .rule{left:420px;top:78px;width:140px;height:3px;background:var(--white)}
.timeline{left:40px;top:300px;width:900px;height:3px;background:var(--white)}
.q{font-size:20px;font-weight:700}
.node{width:16px;height:16px;border-radius:50%;background:var(--white);border:3px solid var(--blue)}
.items{width:210px;font-size:12px;line-height:1.5;list-style:none}
.items li{margin-bottom:8px;padding-left:12px;border-left:2px solid rgba(255,255,255,.7)}
.arrow-btn{width:40px;height:40px;border-radius:50%;background:var(--blue);display:flex;align-items:center;justify-content:center}

/* faq */
.faq-title{left:160px;top:2530px;color:var(--blue)}
.faq-item{left:160px;width:880px;border:1px solid var(--line);border-radius:12px;background:var(--white);padding:0 24px;display:flex;align-items:center;justify-content:space-between;font-size:15px;font-weight:600;color:var(--blue);box-shadow:0 6px 18px rgba(42,26,142,.08)}
.faq-item.open{display:block;padding:22px 24px;border-color:var(--blue)}
.faq-item.open .row{display:flex;justify-content:space-between;align-items:center}
.faq-item p{margin-top:12px;font-size:13px;font-weight:400;color:var(--muted);line-height:1.6;width:760px}
.chev{width:26px;height:26px;border-radius:50%;background:var(--green);display:flex;align-items:center;justify-content:center;flex:none}

/* team */
.team{left:0;top:3240px;width:1200px;height:560px}
.team h2{left:0;top:100px;width:1200px;text-align:center;color:var(--white)}
.member{width:270px;height:290px;border-radius:20px;border:2px solid rgba(255,255,255,.5);background:var(--blue-deep);text-align:center;color:var(--white);padding-top:36px}
.member.lead{background:linear-gradient(160deg,var(--green-light),var(--green));border-color:var(--green-light);height:320px}
.portrait{width:130px;height:130px;border-radius:50%;margin:0 auto;background:linear-gradient(160deg,#b9c2d8,#6c7594);border:4px solid var(--white)}
.member h3{margin-top:20px;font-size:18px;font-weight:600}
.member span{display:block;margin-top:4px;font-size:13px;opacity:.85}

/* footer */
.footer-brand{left:100px;top:3880px}
.copy{left:100px;top:3940px;font-size:12px;color:var(--muted);line-height:1.6}
.fcol{top:3860px;padding-left:18px;border-left:2px solid var(--green)}
.fcol h4{font-size:17px;font-weight:600;color:var(--blue);margin-bottom:10px}
.fcol a{display:block;font-size:13px;color:var(--muted);text-decoration:none;line-height:1.7}
.socials{display:flex;gap:10px}
.socials span{width:34px;height:34px;border-radius:50%;border:2px solid var(--green);display:flex;align-items:center;justify-content:center;font-size:11px;font-weight:600;color:var(--blue)}
</style>
</head>
<body>

<section class="hero abs">
  <div class="forest abs" role="img" aria-label="Forest silhouette at dusk"></div>
  <div class="brand abs" style="left:60px;top:20px"><span class="brand-dot"></span>Germinea</div>
  <nav class="nav abs"><span>How to Protect</span><span>Roadmap</span><span>Join Now</span><span>FAQ</span><span>Team</span></nav>
  <h1 class="abs">Protegeons la nature ensemble</h1>
  <p class="hero-lead abs">Faites un don de tokens et aidez à protéger la faune et flore.</p>
  <p class="hero-text abs">Notre plateforme vous permet d'acheter des tokens de votre choix pour les donner à un projet de protection de la nature. Votre contribution aidera à financer des actions concrètes pour préserver l'environnement.</p>
  <div class="partners abs"><span>Velcor</span><span>Tablewise</span><span>Norvia</span></div>
  <div class="buy abs">
    <h3>Acheter des token</h3>
    <div class="counter"><span class="btn">−</span>12<span class="btn">+</span></div>
    <div class="price">12 token = 30€</div>
    <div class="cta">Acheter</div>
  </div>
  <svg class="abs" style="left:0;top:690px" width="1200" height="52" viewBox="0 0 1200 52"><path d="M0 52 C300 0 900 0 1200 52 Z" fill="#fff"/></svg>
</section>

<h2 class="h2 how-title abs">Comment proteger la nature avec<br>des tokens Germinea ?</h2>

<div class="step filled abs" style="left:440px;top:905px">
  <div class="step-icon"><svg width="30" height="30" viewBox="0 0 24 24" fill="none" stroke="#fff" stroke-width="2"><rect x="5" y="4" width="14" height="16" rx="2"/><path d="M9 12l2 2 4-4"/></svg></div>
  <h3 class="h3">Votez pour un projet</h3>
  <p>Vous pouvez ensuite voter en ligne pour le projet de votre choix. Les projets sont proposés par des associations et des ONG pour la nature.</p>
</div>
<div class="step outline abs" style="left:150px;top:915px">
  <div class="step-icon"><svg width="30" height="30" viewBox="0 0 24 24" fill="none" stroke="#fff" stroke-width="2"><circle cx="12" cy="12" r="8"/><path d="M12 8v8M9 11h6"/></svg></div>
  <h3 class="h3">Achetez des tokens<br>Germinea</h3>
  <p>Les tokens sont des actifs numériques qui servent à financer la faune et les projets des associations.</p>
</div>
<div class="step outline abs" style="left:750px;top:915px">
  <div class="step-icon"><svg width="30" height="30" viewBox="0 0 24 24" fill="none" stroke="#fff" stroke-width="2"><path d="M4 14h4l4 3 6-5"/><circle cx="15" cy="7" r="3"/></svg></div>
  <h3 class="h3">L'association choisit<br>reçoit l'argent</h3>
  <p>Le projet qui aura le plus de votes recevra les tokens pour financer ses actions concrètes.</p>
</div>

<section class="community abs">
  <div class="community-forest abs" role="img" aria-label="Forest silhouette"></div>
  <h2 class="abs">Rejoignez la communaute pour soutenir la protection de la nature</h2>
  <p class="lead abs">La nature est en danger, nous devons agir ensemble. Rejoignez la communauté pour soutenir la protection de la nature.</p>
  <p class="sub abs">En rejoignant la communauté, vous pourrez :</p>
  <ul class="abs">
    <li>Suivre les projets des associations qui travaillent pour la nature.</li>
    <li>Voter pour le projet de votre choix et aider à financer ses actions.</li>
    <li>Être informé des dernières actualités sur la protection de la nature.</li>
  </ul>
  <div class="laptop abs" role="img" aria-label="Laptop showing the community channels"></div>
  <div class="channels abs"><span>Talkhaven</span><span>Postline</span></div>
</section>

<section class="roadmap abs">
  <h2 class="abs">Roadmap</h2>
  <div class="rule abs"></div>
  <div class="timeline abs"></div>
  <span class="node abs" style="left:52px;top:294px"></span>
  <span class="node abs" style="left:300px;top:294px"></span>
  <span class="node abs" style="left:560px;top:294px"></span>
  <span class="node abs" style="left:880px;top:294px"></span>
  <span class="q abs" style="left:40px;top:318px">Q1 2024</span>
  <span class="q abs" style="left:300px;top:262px">Q2 2024</span>
  <span class="q abs" style="left:560px;top:318px">Q3 2024</span>
  <span class="q abs" style="left:850px;top:262px">Q4 2024</span>
  <ul class="items abs" style="left:60px;top:120px"><li>Site internet &amp; réseaux sociaux</li><li>Marketing &amp; Développement du smart contract token</li><li>Lancement de la prévente</li><li>Développement du smart contract token</li></ul>
  <ul class="items abs" style="left:310px;top:340px"><li>Site internet &amp; réseaux sociaux</li><li>Marketing &amp; Développement du smart contract token</li></ul>
  <ul class="items abs" style="left:570px;top:120px"><li>Site internet &amp; réseaux sociaux</li><li>Marketing &amp; Développement du smart contract token</li><li>Lancement de la vente</li><li>Développement du smart contract</li></ul>
  <ul class="items abs" style="left:860px;top:340px;width:110px"><li>Site internet</li><li>Marketing</li><li>Nouveaux projets</li></ul>
  <div class="abs" style="left:440px;top:500px;display:flex;gap:16px">
    <span class="arrow-btn"><svg width="16" height="16" viewBox="0 0 24 24" fill="none" stroke="#fff" stroke-width="3"><path d="M15 5l-7 7 7 7"/></svg></span>
    <span class="arrow-btn"><svg width="16" height="16" viewBox="0 0 24 24" fill="none" stroke="#fff" stroke-width="3"><path d="M9 5l7 7-7 7"/></svg></span>
  </div>
</section>

<h2 class="h2 faq-title abs">Frequently Asked Questions</h2>
<div class="faq-item open abs" style="top:2610px">
  <div class="row">Lorem ipsum dolor sit amet consectetur adipiscing elit sed do eiusmod ?<span class="chev"><svg width="12" height="12" viewBox="0 0 24 24" fill="none" stroke="#fff" stroke-width="3"><path d="M5 15l7-7 7 7"/></svg></span></div>
  <p>Lorem ipsum dolor sit amet, consectetur adipiscing elit, sed do eiusmod tempor incididunt ut labore et dolore magna aliqua. Quis ipsum suspendisse ultrices gravida. Risus commodo viverra maecenas accumsan lacus vel facilisis.</p>
</div>
<div class="faq-item abs" style="top:2770px;height:58px">Aenean incididunt ut labore et dolore magna aliqu ?<span class="chev"><svg width="12" height="12" viewBox="0 0 24 24" fill="none" stroke="#fff" stroke-width="3"><path d="M5 9l7 7 7-7"/></svg></span></div>
<div class="faq-item abs" style="top:2846px;height:58px">Ut enim ad minim veniam, quis nostrud exercitation ullamco ?<span class="chev"><svg width="12" height="12" viewBox="0 0 24 24" fill="none" stroke="#fff" stroke-width="3"><path d="M5 9l7 7 7-7"/></svg></span></div>
<div class="faq-item abs" style="top:2922px;height:58px">Laboris nisi ut aliquip ex ea commodo consequa ?<span class="chev"><svg width="12" height="12" viewBox="0 0 24 24" fill="none" stroke="#fff" stroke-width="3"><path d="M5 9l7 7 7-7"/></svg></span></div>
<div class="faq-item abs" style="top:2998px;height:58px">Duis aute irure dolor in reprehenderit in voluptate velit esse ?<span class="chev"><svg width="12" height="12" viewBox="0 0 24 24" fill="none" stroke="#fff" stroke-width="3"><path d="M5 9l7 7 7-7"/></svg></span></div>
<div class="faq-item abs" style="top:3074px;height:58px">Fillum dolore eu fugiat nulla pariatur ?<span class="chev"><svg width="12" height="12" viewBox="0 0 24 24" fill="none" stroke="#fff" stroke-width="3"><path d="M5 9l7 7 7-7"/></svg></span></div>

<section class="team abs">
  <svg class="abs" style="left:0;top:0" width="1200" height="560" viewBox="0 0 1200 560"><path d="M0 60 C300 0 900 0 1200 60 L1200 500 C900 560 300 560 0 500 Z" fill="#2a1a8e"/></svg>
  <h2 class="h2 abs">Our Team</h2>
  <div class="member abs" style="left:150px;top:190px"><div class="portrait" role="img" aria-label="Portrait of Hollenbeck Adrien"></div><h3>Hollenbeck<br>Adrien</h3><span>Fondateur</span></div>
  <div class="member lead abs" style="left:465px;top:180px"><div class="portrait" role="img" aria-label="Portrait of Marchal Elise"></div><h3>Marchal Elise</h3><span>Developpeur<br>blockchain</span></div>
  <div class="member abs" style="left:780px;top:190px"><div class="portrait" role="img" aria-label="Portrait of Ferrand Lucie"></div><h3>Ferrand Lucie</h3><span>Developpeur front-end</span></div>
</section>

<div class="brand footer-brand abs" style="color:var(--blue)"><span class="brand-dot"></span>Germinea</div>
<p class="copy abs">© 2024 Germinea<br>All rights reserved.</p>
<div class="fcol abs" style="left:420px"><h4>Quick Links</h4><a>How to Protect</a><a>Roadmap</a><a>Join Now</a><a>FAQ</a><a>Team</a></div>
<div class="fcol abs" style="left:650px"><h4>Resources</h4><a>Support</a><a>Why Us</a><a>Benefits</a><a>Contact Us</a></div>
<div class="fcol abs" style="left:880px"><h4>Stay in touch</h4><div class="socials"><span>Ln</span><span>Pl</span><span>Sg</span></div></div>

</body>
</html>
```